Wedding Thank You post card

We would like to design a thank you post card for our wedding guests.
We want it to be a classic style with our photo and a simple 'Thank you' written and then Tom and Sylvia 15.03.2014' Where the writing does not obstruct our image.
We need 140 post cards
Sorry for the delay please find some photos you can use for the design process. One or all photos can be used. Thank you
Wedding

```html
<!DOCTYPE html>
<html lang="en">
<head>
<meta charset="utf-8">
<title>Wedding Thank You Post Card</title>
<link rel="stylesheet" href="https://fonts.googleapis.com/css2?family=Great+Vibes&family=Parisienne&display=swap">
<style>
  :root {
    --backdrop: #7d7d7d;
    --sage-light: #f6f8e4;
    --sage-mid: #dfe6b4;
    --sage-deep: #c9d48f;
    --band-white: #ffffff;
    --ink-white: #ffffff;
    --sky: #a9c6e6;
    --stone: #b9ab95;
    --lawn: #c9b23a;
    --asphalt: #4a4a4e;
  }
  * { margin: 0; padding: 0; box-sizing: border-box; }
  html, body {
    width: 1200px;
    height: 1000px;
    overflow: hidden;
    background: var(--backdrop);
  }
  .postcard {
    position: absolute;
    left: 52px;
    top: 20px;
    width: 1108px;
    height: 858px;
    overflow: hidden;
    background: var(--band-white);
  }
  .postcard__art {
    position: absolute;
    inset: 0;
    width: 1108px;
    height: 858px;
  }
  .greeting {
    position: absolute;
    color: var(--ink-white);
    font-family: "Great Vibes", cursive;
    font-weight: 400;
    line-height: 1;
    text-align: center;
    text-shadow: 1px 2px 3px rgba(90, 100, 40, 0.35);
    white-space: nowrap;
  }
  .greeting--thank { left: 600px; width: 500px; top: 150px; font-size: 168px; }
  .greeting--you   { left: 620px; width: 440px; top: 330px; font-size: 168px; }
  .couple-names {
    position: absolute;
    left: 590px;
    width: 490px;
    top: 552px;
    text-align: center;
    color: var(--ink-white);
    font-family: "Parisienne", cursive;
    font-size: 60px;
    line-height: 1;
    text-shadow: 1px 2px 3px rgba(90, 100, 40, 0.3);
    white-space: nowrap;
  }
  .wedding-date {
    position: absolute;
    left: 640px;
    width: 400px;
    top: 630px;
    text-align: center;
    color: var(--ink-white);
    font-family: "Parisienne", cursive;
    font-size: 38px;
    line-height: 1;
    letter-spacing: 1px;
    text-shadow: 1px 2px 3px rgba(90, 100, 40, 0.3);
  }
</style>
</head>
<body>
  <main class="postcard">
    <svg class="postcard__art" viewBox="0 0 1108 858" xmlns="http://www.w3.org/2000/svg">
      <defs>
        <linearGradient id="photoTones" x1="0" y1="0" x2="0" y2="1">
          <stop offset="0" stop-color="var(--sky)"/>
          <stop offset="0.3" stop-color="#dfe3e6"/>
          <stop offset="0.38" stop-color="var(--stone)"/>
          <stop offset="0.47" stop-color="var(--lawn)"/>
          <stop offset="0.53" stop-color="#5a5a5e"/>
          <stop offset="1" stop-color="var(--asphalt)"/>
        </linearGradient>
        <radialGradient id="sageSheen" cx="0.55" cy="0.45" r="0.8">
          <stop offset="0" stop-color="var(--sage-light)"/>
          <stop offset="0.55" stop-color="var(--sage-mid)"/>
          <stop offset="1" stop-color="var(--sage-deep)"/>
        </radialGradient>
        <linearGradient id="sageBands" x1="0" y1="0" x2="0" y2="1">
          <stop offset="0" stop-color="#ffffff" stop-opacity="0.35"/>
          <stop offset="0.25" stop-color="#ffffff" stop-opacity="0"/>
          <stop offset="0.45" stop-color="#ffffff" stop-opacity="0.3"/>
          <stop offset="0.7" stop-color="#ffffff" stop-opacity="0"/>
          <stop offset="1" stop-color="#ffffff" stop-opacity="0.4"/>
        </linearGradient>
      </defs>
      <g class="wedding-photo" role="img" aria-label="Wedding photo: bride and groom on a driveway in front of a stone castle on a sunny day">
        <path d="M0 0 H483 C560 100 580 250 540 420 C510 560 500 700 568 858 H0 Z" fill="url(#photoTones)"/>
      </g>
      <g class="sage-panel" role="img" aria-label="Soft sage green panel with a faint damask pattern">
        <path d="M528 0 C600 110 610 270 560 430 C520 560 530 720 628 858 H1108 V0 Z" fill="url(#sageSheen)"/>
        <path d="M528 0 C600 110 610 270 560 430 C520 560 530 720 628 858 H1108 V0 Z" fill="url(#sageBands)"/>
      </g>
    </svg>
    <h1 class="greeting greeting--thank">Thank</h1>
    <p class="greeting greeting--you">You</p>
    <p class="couple-names">Tom &amp; Sylvia</p>
    <p class="wedding-date">15.03.2014</p>
  </main>
</body>
</html>
```